Business Telephone Service Brochure

I need a brochure designed to help sell our VoIP service. The brochure needs to be clean, attention getting, professional and have 3 key areas of information (Key Features, Benefits & Service Plans). Here is an idea of what we are looking for https://www.plenvora.com/design/24930587. Need to also include how much the customer could save. See this for an example https://quarbeline.com/postcard-flyer-design/contests/voip-sales-flyer-template-replicate-attached-582913. The Service Plan section needs to allow room for two types of plans. One plan includes the phone and has a 12, 24 and 36 month option. Each term (12,24,36) will have its own monthly cost per device. The second service option is no-commitment monthly with a single per month price per device. The included features section should allow for up to 16 features to be listed. The benefits should allow for 4-6 benefits to be listed. Also include room for Logo, business address, website, phone number and email.

Target Market(s)

Small to medium business with 1-100 employees.

Industry/Entity Type

Telecommunications

Font styles to use
Serif

Colors

Designer to choose colors to be used in the design.

Requirements
Must have
• Key Feature, Benefits and Service Plans (i.e. Pricing). Company logo, phone, email and website. Must have "Save up to x%!" and catch attention.
Nice to have
• Limited colors. I am not setting a hard limit, please take the liberty to do what you feel is needed. Just keep in mind we want it to be clean, professional and attention getting without being to flashy or obnoxious.
Should not have
• Nothing busy or distracting.

```html
<!DOCTYPE html>
<html lang="en">
<head>
<meta charset="utf-8">
<title>Telvano Business Telephone Brochure</title>
<link href="https://fonts.googleapis.com/css2?family=Lato:wght@400;700;900&family=Roboto+Condensed:wght@300;400;700&family=Oswald:wght@400;700&display=swap" rel="stylesheet">
<style>
:root{
  --navy:#232a6e;
  --navy-deep:#1c2260;
  --accent:#3b3fc1;
  --accent-soft:#4a4fd0;
  --ink:#1a1a1a;
  --paper:#ffffff;
  --stage:#d6d6d6;
  --rule:#8a8a8a;
  --dark:#1c1c1f;
  --cell:#3a3a3e;
}
*{box-sizing:border-box;margin:0;padding:0}
html,body{width:1200px;height:1200px;overflow:hidden;background:var(--stage);font-family:'Lato',sans-serif;color:var(--ink)}
sup{font-size:.7em;line-height:0;vertical-align:super}
.page{position:absolute;top:240px;width:524px;height:720px;background:var(--paper);overflow:hidden}
.page--front{left:50px}
.page--back{left:618px}

/* brand */
.brand{position:absolute;text-align:center;color:var(--navy)}
.brand__name{font-family:'Lato',sans-serif;font-weight:900;letter-spacing:-1px;line-height:1}
.brand__tag{font-family:'Roboto Condensed',sans-serif;color:#666;margin-top:3px}

/* hero */
.hero{position:absolute;left:0;top:116px;width:524px;height:290px}
.hero__photo{position:absolute;inset:0;background:linear-gradient(100deg,#2a2c33 0%,#4b4d55 45%,#c9c4c0 80%,#e6e2de 100%)}
.hero__panel{position:absolute;inset:0}
.hero__lead{position:absolute;left:28px;top:42px;font-size:19px;line-height:23px;color:#fff}
.hero__lead b{color:#5358e0;font-weight:700}
.hero__save{position:absolute;left:28px;top:134px;font-family:'Roboto Condensed',sans-serif;font-weight:300;font-size:46px;color:#fff;letter-spacing:1px}
.hero__upto{position:absolute;left:31px;top:174px;font-family:'Oswald',sans-serif;font-weight:700;font-size:20px;line-height:22px;color:#fff;transform:scaleX(.85);transform-origin:left}
.hero__pct{position:absolute;left:30px;top:186px;font-family:'Oswald',sans-serif;font-weight:700;font-size:92px;color:#fff;letter-spacing:-3px;line-height:1.1}

/* features */
.features{position:absolute;left:0;top:406px;width:524px;height:250px;background:linear-gradient(180deg,#f2f2f3,#ffffff 70%)}
.section-title{font-family:'Roboto Condensed',sans-serif;font-size:17px;color:var(--navy);display:flex;align-items:center;gap:6px}
.section-title b{font-weight:700}
.features .features-title{position:absolute;left:186px;top:14px}
.features .contact-title{position:absolute;left:186px;top:222px}
.feature-list{position:absolute;list-style:none;font-size:9.3px;line-height:11px}
.feature-list li{position:relative;padding-left:21px;height:21px}
.feature-list li::before{content:"";position:absolute;left:0;top:1px;width:7px;height:7px;border:1.2px solid #555;border-radius:50%}
.feature-list li::after{content:"";position:absolute;left:7px;top:8px;width:3px;height:1.2px;background:#555;transform:rotate(45deg)}
.feature-list--a{left:54px;top:52px}
.feature-list--b{left:294px;top:52px}
.feature-list li.tall{height:32px}

.footer{position:absolute;left:0;top:656px;width:524px;height:64px;background:var(--navy)}
.footer::after{content:"";position:absolute;left:0;bottom:0;width:100%;height:14px;background:#2a3284}
.footer__items{position:absolute;left:50px;top:14px;display:flex;gap:26px;align-items:center;color:#fff;font-size:12px}
.footer__item{display:flex;align-items:center;gap:8px}
.footer__phone{font-weight:900;font-size:14px;letter-spacing:.5px}

/* benefits */
.benefits-title{position:absolute;left:194px;top:26px;font-size:17px}
.benefit{position:absolute;width:150px;text-align:center;font-size:11.5px;line-height:13px;color:#222}
.benefit b{display:block;color:var(--navy);font-weight:700}
.benefit svg{display:block;margin:0 auto 6px}
.rule-v{position:absolute;width:1px;background:var(--rule);top:82px;height:180px}
.rule-h{position:absolute;height:1px;background:var(--rule);top:178px;width:86px}

/* pricing */
.pricing{position:absolute;left:0;top:293px;width:524px;height:427px;background:var(--dark)}
.pricing__scene{position:absolute;inset:0;background:linear-gradient(160deg,#2b2b30 0%,#151518 55%,#222226 100%)}
.pricing .section-title{position:absolute;left:200px;top:20px;color:#fff}
.price-table{position:absolute;left:38px;top:61px;border-collapse:separate;border-spacing:2px;font-size:8.6px;color:#fff}
.price-table th{font-weight:400;font-size:11px;line-height:12px;height:33px;vertical-align:top;padding-top:5px;text-align:center;background:var(--accent-soft)}
.price-table th.svc{background:var(--cell);text-align:left;padding-left:9px;font-weight:700;width:160px}
.price-table td{background:var(--cell);height:24px;text-align:center}
.price-table td.svc{text-align:left;padding-left:9px;line-height:10px}
.note{position:absolute;left:38px;width:437px;height:18px;background:var(--accent);color:#fff;font-size:8.4px;line-height:18px;padding-left:7px;border-bottom:1px solid #aab;white-space:nowrap;overflow:hidden}

.back-shape{position:absolute;inset:0}
.back-brand{position:absolute;left:36px;top:548px;text-align:left}
.back-contact{position:absolute;left:36px;top:618px}
.contact-lines{position:absolute;left:38px;top:645px;font-size:11.5px;line-height:15.5px;color:#222}
.contact-lines div{display:flex;align-items:center;gap:9px}
.contact-lines .phone{font-weight:900;font-size:13px;letter-spacing:.5px}
.handset{position:absolute;left:244px;top:520px;width:236px;height:186px;border-radius:18px;background:linear-gradient(150deg,#3a3b40,#111114 70%);transform:rotate(-14deg)}
</style>
</head>
<body>

<section class="page page--front">
  <div class="brand" style="left:0;width:524px;top:28px">
    <div class="brand__name" style="font-size:52px">Telvano</div>
    <div class="brand__tag" style="font-size:8.5px">Internet-Telephone-Security-Networking</div>
  </div>

  <div class="hero">
    <div class="hero__photo" role="img" aria-label="Photo of smiling call centre agents wearing headsets"></div>
    <svg class="hero__panel" width="524" height="290" viewBox="0 0 524 290">
      <polygon points="0,0 152,0 214,290 0,290" fill="#25262c" opacity=".88"/>
      <polygon points="0,210 214,290 0,290" fill="#2a3284"/>
      <polygon points="60,290 214,290 190,232" fill="#2a3284"/>
    </svg>
    <div class="hero__lead"><b>Lorem Ipsum</b><br>is simply<br>dummy text</div>
    <div class="hero__save">SAVE</div>
    <div class="hero__upto">UP TO</div>
    <div class="hero__pct">X%!</div>
  </div>

  <div class="features">
    <div class="section-title features-title">
      <svg width="18" height="20" viewBox="0 0 18 20"><rect x="1" y="1" width="13" height="17" fill="none" stroke="#333" stroke-width="1.3"/><line x1="4" y1="7" x2="11" y2="7" stroke="#333"/><line x1="4" y1="10" x2="9" y2="10" stroke="#333"/><circle cx="13" cy="15" r="3" fill="none" stroke="#3b3fc1" stroke-width="1.4"/></svg>
      <span><b>KEY</b> FEATURES</span>
    </div>
    <ul class="feature-list feature-list--a">
      <li>Unlimited local and long distance calling</li>
      <li>HD Voice</li>
      <li>Business SMS/Text Messaging</li>
      <li>Personal and Shared Voicemail Boxes</li>
      <li>Audio Conferencing</li>
      <li>Intercom</li>
      <li>Mobile App</li>
      <li>Auto Attendant/Interactive Voice Routing</li>
    </ul>
    <ul class="feature-list feature-list--b">
      <li>Free web or email fax</li>
      <li>Web admin portal</li>
      <li>Music On Hold - Customizable</li>
      <li>Redundancy/Failover – Never miss a call</li>
      <li>Lorem Ipsum is simply dummy text</li>
      <li class="tall">Lorem Ipsum is simply dummy text<br>of the printing</li>
      <li>Lorem Ipsum is simply dummy text</li>
      <li>Lorem Ipsum is simply dummy text</li>
    </ul>
    <div class="section-title contact-title">
      <svg width="20" height="20" viewBox="0 0 20 20"><rect x="1" y="2" width="14" height="16" fill="none" stroke="#333" stroke-width="1.3"/><circle cx="13" cy="6" r="3.5" fill="none" stroke="#3b3fc1" stroke-width="1.4"/></svg>
      <span><b>CONTACT</b> US :</span>
    </div>
  </div>

  <footer class="footer">
    <div class="footer__items">
      <div class="footer__item">
        <svg width="14" height="14" viewBox="0 0 14 14"><circle cx="7" cy="7" r="6.3" fill="none" stroke="#fff" stroke-width="1.2"/><path d="M4.5 4 L6 4 L6.5 6 L5.6 6.6 Q6.5 8.4 7.4 8.6 L8 7.7 L10 8.2 L10 9.6 Q6 10 4.5 4Z" fill="#fff"/></svg>
        <span class="footer__phone">XXX-XXXX-XX</span>
      </div>
      <div class="footer__item">
        <svg width="14" height="14" viewBox="0 0 14 14"><circle cx="7" cy="7" r="6.3" fill="none" stroke="#fff" stroke-width="1.2"/><rect x="4" y="5" width="6" height="4.2" fill="none" stroke="#fff"/><path d="M4 5 L7 7.3 L10 5" fill="none" stroke="#fff"/></svg>
        <span>your mail id here</span>
      </div>
      <div class="footer__item">
        <svg width="14" height="14" viewBox="0 0 14 14"><circle cx="7" cy="7" r="6.3" fill="none" stroke="#fff" stroke-width="1.2"/><ellipse cx="7" cy="7" rx="2.2" ry="4" fill="none" stroke="#fff" stroke-width=".9"/><line x1="3" y1="7" x2="11" y2="7" stroke="#fff" stroke-width=".9"/></svg>
        <span>www.yourwebsite.com</span>
      </div>
    </div>
  </footer>
</section>

<section class="page page--back">
  <div class="section-title benefits-title">
    <svg width="26" height="24" viewBox="0 0 26 24"><circle cx="11" cy="11" r="9" fill="none" stroke="#333" stroke-width="1.3"/><circle cx="8" cy="9" r="2.5" fill="none" stroke="#333"/><line x1="17" y1="17" x2="23" y2="23" stroke="#333" stroke-width="1.6"/><rect x="13" y="11" width="2" height="4" fill="#3b3fc1"/></svg>
    <b>BENEFITS</b>
  </div>

  <div class="benefit" style="left:21px;top:74px">
    <svg width="34" height="36" viewBox="0 0 34 36"><rect x="6" y="2" width="26" height="30" fill="none" stroke="#222" stroke-width="1.3" stroke-dasharray="3 2"/><text x="19" y="24" text-anchor="middle" font-family="Lato" font-size="20" fill="#3b3fc1">$</text><path d="M1 28 L7 35 M7 28 L1 35" stroke="#222" stroke-width="1.3"/></svg>
    <b>No expensive</b>onsite telephone<br>equipment
  </div>
  <div class="benefit" style="left:181px;top:70px">
    <svg width="44" height="44" viewBox="0 0 44 44"><circle cx="22" cy="22" r="20" fill="var(--navy)"/><circle cx="22" cy="22" r="14" fill="none" stroke="#fff" stroke-width="2"/><path d="M22 8 L22 22 L32 26" fill="none" stroke="#fff" stroke-width="3"/></svg>
    <b>Easily</b>scale up or down<br>and needs change
  </div>
  <div class="benefit" style="left:342px;top:72px">
    <svg width="46" height="40" viewBox="0 0 46 40"><path d="M2 14 Q6 32 20 38 L20 30 Q12 26 10 16Z M44 14 Q40 32 26 38 L26 30 Q34 26 36 16Z" fill="#222"/><rect x="13" y="4" width="20" height="14" fill="none" stroke="var(--navy)" stroke-width="1.5"/><path d="M13 4 L23 12 L33 4" fill="none" stroke="var(--navy)" stroke-width="1.5"/></svg>
    <b>Free</b>telephone/email<br>support
  </div>

  <div class="rule-h" style="left:61px"></div>
  <div class="rule-h" style="left:213px"></div>
  <div class="rule-h" style="left:374px"></div>
  <div class="rule-v" style="left:170px"></div>
  <div class="rule-v" style="left:342px"></div>

  <div class="benefit" style="left:21px;top:202px">
    <svg width="34" height="32" viewBox="0 0 34 32"><rect x="3" y="6" width="6" height="26" fill="#222"/><rect x="12" y="14" width="6" height="18" fill="#222"/><rect x="21" y="22" width="6" height="10" fill="#222"/><path d="M14 2 L30 18" stroke="var(--navy)" stroke-width="2"/><path d="M24 18 L31 19 L30 12" fill="none" stroke="var(--navy)" stroke-width="2"/></svg>
    <b>Lower</b>monthly cost
  </div>
  <div class="benefit" style="left:181px;top:196px">
    <svg width="46" height="38" viewBox="0 0 46 38"><text x="24" y="22" text-anchor="middle" font-family="Lato" font-weight="700" font-size="26" fill="var(--navy)">$</text><path d="M2 26 L14 26 Q22 28 28 30 L42 26 Q44 30 30 36 L2 36Z" fill="#222"/></svg>
    <b>Increase</b>reliability
  </div>
  <div class="benefit" style="left:342px;top:198px">
    <svg width="44" height="36" viewBox="0 0 44 36"><rect x="4" y="2" width="24" height="17" fill="none" stroke="#222" stroke-width="2"/><rect x="7" y="5" width="18" height="11" fill="var(--navy)"/><rect x="12" y="20" width="8" height="4" fill="#222"/><circle cx="33" cy="19" r="5" fill="#222"/><path d="M24 36 Q26 26 33 26 Q40 26 42 36Z" fill="#222"/></svg>
    <b>Easy</b>self-administration
  </div>

  <div class="pricing">
    <div class="pricing__scene" role="img" aria-label="Dark photo of office buildings seen from below"></div>
    <div class="section-title">
      <svg width="28" height="28" viewBox="0 0 28 28"><circle cx="14" cy="10" r="8" fill="none" stroke="#fff" stroke-width="1.4"/><text x="14" y="14" text-anchor="middle" font-family="Lato" font-size="11" fill="#fff">$</text><path d="M2 22 L10 20 L20 23 L26 20" fill="none" stroke="#fff" stroke-width="1.4"/></svg>
      <b>PRICING</b>
    </div>
    <table class="price-table">
      <tr><th class="svc">SERVICE</th><th style="width:68px">MONTHLY</th><th style="width:67px">12 MONTH<br>TERM</th><th style="width:66px">24 MONTH<br>TERM</th><th style="width:66px">36 MONTH<br>TERM</th></tr>
      <tr><td class="svc"><sup>1</sup>Phone service only(phone sold<br>separately)</td><td>$21.95</td><td></td><td></td><td></td></tr>
      <tr><td class="svc">Service + <sup>2</sup>Corvane K20 Phone</td><td></td><td>$24.95</td><td>$22.95</td><td>$20.95</td></tr>
    </table>
    <div class="note" style="top:161px"><sup>1</sup>For monthly service you may purchase <b>the Corvane K20 phone for $65 each,</b> less taxes and shipping.</div>
    <div class="note" style="top:183px"><sup>2</sup><b>Corvane K20 phones are rented</b> and due upon cancellation. Customer pays return shipping.</div>
  </div>

  <svg class="back-shape" width="524" height="720" viewBox="0 0 524 720">
    <polygon points="0,505 524,683 524,720 0,720" fill="#e4e4e6"/>
    <polygon points="0,505 360,627 138,720 0,720" fill="#e4e4e6"/>
    <polygon points="138,720 524,536 524,720" fill="var(--navy)"/>
  </svg>

  <div class="handset" role="img" aria-label="Photo of a black desk IP phone with colour screen"></div>

  <div class="brand back-brand">
    <div class="brand__name" style="font-size:38px">Telvano</div>
    <div class="brand__tag" style="font-size:6px">Internet-Telephone-Security-Networking</div>
  </div>
  <div class="section-title back-contact">
    <svg width="20" height="20" viewBox="0 0 20 20"><rect x="1" y="2" width="14" height="16" fill="none" stroke="#333" stroke-width="1.3"/><circle cx="13" cy="6" r="3.5" fill="none" stroke="#3b3fc1" stroke-width="1.4"/></svg>
    <span><b>CONTACT</b> US :</span>
  </div>
  <div class="contact-lines">
    <div><svg width="10" height="10" viewBox="0 0 10 10"><circle cx="5" cy="5" r="4.4" fill="none" stroke="#444"/><path d="M3 3 L4.2 3 L4.5 4.5 L4 5 Q4.6 6 5.3 6.2 L5.8 5.6 L7 6 L7 7 Q4 7.3 3 3Z" fill="#444"/></svg><span class="phone">XXX-XXXX-XX</span></div>
    <div><svg width="10" height="10" viewBox="0 0 10 10"><rect x="1" y="2.5" width="8" height="5.5" fill="none" stroke="#444"/><path d="M1 2.5 L5 5.5 L9 2.5" fill="none" stroke="#444"/></svg><span>your mail id here</span></div>
    <div><svg width="10" height="10" viewBox="0 0 10 10"><circle cx="5" cy="5" r="4.4" fill="none" stroke="#444"/><ellipse cx="5" cy="5" rx="1.8" ry="4.4" fill="none" stroke="#444" stroke-width=".8"/><line x1="0.6" y1="5" x2="9.4" y2="5" stroke="#444" stroke-width=".8"/></svg><span>www.yourwebsite.com</span></div>
  </div>
</section>

</body>
</html>
```